We want to design total new business card and logo for Korvel Building Services Ltd

Our company name Korvel Building Services Ltd. Design new logo and business card , need hi-end luxury style art for architecture and construction industry. The card should simple but stylish. Our business focus on CONNECT tradesman to construction company, help marketing construction company tender oversea projects, managing franchise in construction sector, delivery amazing services to our client, so Logo should show the CONNECTION IDEA, CONNECTING PEOPLE, LUXURY. Visit our website for more information: korvelhub.co.nz

Target Market(s)

Directors or managers

Industry/Entity Type

Construction Company

Contact Information for Business Card

Name, Title, Mobile, Email, Website

Font styles to use
Serif

Colors

Designer to choose colors to be used in the design.

Requirements
Must have
• Simple and luxury, connection icon
Nice to have
• Special materials, plastic card, look through,...
• Look new ideas.

```html
<!DOCTYPE html>
<html lang="en">
<head>
<meta charset="utf-8">
<title>Korvel Building Services Ltd – Business Card</title>
<link rel="stylesheet" href="https://fonts.googleapis.com/css2?family=Tinos:wght@400;700&display=swap">
<style>
  :root {
    --stage: #2a2b2e;
    --card: #1f2124;
    --card-deep: #0d0e10;
    --teal: #1fa2b8;
    --silver: #d9d9dc;
    --ink-light: #e8e8ea;
    --serif: "Tinos", "Times New Roman", serif;
  }
  * { margin: 0; padding: 0; box-sizing: border-box; }
  html, body { width: 1200px; height: 800px; overflow: hidden; }
  body {
    background: var(--stage);
    font-family: var(--serif);
    display: flex;
    align-items: center;
    justify-content: center;
    gap: 40px;
  }
  .card {
    position: relative;
    width: 540px;
    height: 310px;
    background: var(--card);
    border-radius: 18px;
    overflow: hidden;
    box-shadow: 0 18px 40px rgba(0,0,0,.45);
  }

  /* Back of card */
  .card-back .pattern-area {
    position: absolute;
    left: 0; bottom: 0;
    width: 340px; height: 310px;
    background: radial-gradient(circle at 15% 95%, var(--card-deep) 0%, rgba(13,14,16,.8) 40%, rgba(31,33,36,0) 70%);
  }
  .card-back .brand {
    position: absolute;
    right: 70px; top: 70px;
    display: flex; align-items: center; gap: 12px;
  }
  .brand-dot {
    width: 22px; height: 22px; border-radius: 50%;
    background: var(--silver);
  }
  .card-back .brand-name {
    font-size: 34px; color: var(--silver); letter-spacing: 2px;
  }
  .card-back .website {
    position: absolute;
    right: 70px; top: 150px;
    font-size: 15px; color: var(--ink-light); letter-spacing: .5px;
  }
  .website .domain { color: var(--teal); }

  /* Front of card */
  .card-front .brand-block {
    position: absolute;
    left: 22px; top: 96px;
    width: 254px;
    text-align: center;
  }
  .card-front .brand-mark {
    display: flex; align-items: center; justify-content: center; gap: 10px;
    margin-bottom: 14px;
  }
  .card-front .brand-mark .brand-dot { background: var(--teal); width: 26px; height: 26px; }
  .card-front .brand-name {
    font-size: 30px; color: var(--teal); letter-spacing: 2px;
  }
  .card-front .company {
    font-size: 12px; color: var(--teal); letter-spacing: .6px;
    white-space: nowrap;
    padding-bottom: 6px;
    border-bottom: 1.5px solid var(--teal);
  }
  .card-front .divider {
    position: absolute;
    left: 290px; top: 60px;
    width: 1px; height: 190px;
    background: var(--teal);
  }
  .card-front .details {
    position: absolute;
    left: 312px; top: 56px;
    color: var(--ink-light);
  }
  .person-name { font-size: 26px; font-weight: 700; color: var(--teal); line-height: 1; }
  .person-title { font-size: 14px; margin-top: 4px; }
  .address { font-size: 13px; margin-top: 12px; line-height: 1.35; }
  .contact-list { list-style: none; margin-top: 14px; }
  .contact-list li {
    display: flex; align-items: center; gap: 8px;
    font-size: 13px; line-height: 1; margin-bottom: 7px;
  }
  .contact-list svg { width: 16px; height: 16px; flex: none; }
</style>
</head>
<body>

  <section class="card card-back" aria-label="Card back">
    <div class="pattern-area" role="img" aria-label="Decorative pattern of scattered rounded black squares"></div>
    <div class="brand">
      <span class="brand-dot"></span>
      <span class="brand-name">Korvel</span>
    </div>
    <p class="website">www.<span class="domain">korvelhub</span>.co.nz</p>
  </section>

  <section class="card card-front" aria-label="Card front">
    <div class="brand-block">
      <div class="brand-mark">
        <span class="brand-dot"></span>
        <span class="brand-name">Korvel</span>
      </div>
      <p class="company">KORVEL BUILDING SERVICES LTD</p>
    </div>

    <div class="divider"></div>

    <div class="details">
      <p class="person-name">Rowan Hale</p>
      <p class="person-title">Manager</p>
      <p class="address">PO Box 418, Harbour Road<br>Level 3, Auckland 1010</p>
      <ul class="contact-list">
        <li>
          <svg viewBox="0 0 16 16" aria-hidden="true"><circle cx="8" cy="8" r="7.5" fill="#1fa2b8"/><rect x="5.5" y="3.5" width="5" height="9" rx="1" fill="none" stroke="#1f2124" stroke-width="1.2"/></svg>
          021 384 6072
        </li>
        <li>
          <svg viewBox="0 0 16 16" aria-hidden="true"><circle cx="8" cy="8" r="7.5" fill="#1fa2b8"/><rect x="4" y="5" width="8" height="6" fill="none" stroke="#1f2124" stroke-width="1.2"/><path d="M4 5l4 3.5L12 5" fill="none" stroke="#1f2124" stroke-width="1.2"/></svg>
          info@korvelhub.co.nz
        </li>
        <li>
          <svg viewBox="0 0 16 16" aria-hidden="true"><circle cx="8" cy="8" r="7.5" fill="#1fa2b8"/><circle cx="8" cy="8" r="4" fill="none" stroke="#1f2124" stroke-width="1.2"/><path d="M4 8h8M8 4c-2 2.5-2 5.5 0 8M8 4c2 2.5 2 5.5 0 8" fill="none" stroke="#1f2124" stroke-width="1"/></svg>
          <span class="website">www.<span class="domain">korvelhub</span>.co.nz</span>
        </li>
      </ul>
    </div>
  </section>

</body>
</html>
```